I would like to start a new webpage for a dating site in switzerland.
The dating site is not a escort service at all and should not transmit any type of sexual connotation.
The is more a compagnionship dating : male pay to meet ladies for some time in which they invite them for dinner, coktail, museum visit or walking or even skying. the meeting will take place in big cities in switzerland: geneva, zurich, bern, lausannes.

```html
<!DOCTYPE html>
<html lang="en">
<head>
<meta charset="utf-8">
<title>Evening Company – Companionship Dating in Switzerland</title>
<link href="https://fonts.googleapis.com/css2?family=Signika:wght@300;400&family=Open+Sans:wght@400&family=Roboto:wght@400;700&display=swap" rel="stylesheet">
<style>
  :root {
    --red: #d7001f;
    --dark-band: #2a2628;
    --gold: #e9a24c;
    --ink: #2d3a4a;
    --heading-brown: #3b1f22;
    --body-grey: #555555;
    --label-grey: #8a8a8a;
    --age-red: #e0606a;
    --dot-grey: #7c8595;
    --white: #ffffff;
  }
  * { margin: 0; padding: 0; box-sizing: border-box; }
  html, body { width: 960px; height: 1200px; overflow: hidden; background: var(--white); }
  body { position: relative; font-family: Arial, Helvetica, sans-serif; }

  .hero {
    position: absolute; left: 0; top: 0; width: 960px; height: 433px;
    background: linear-gradient(100deg, #5a3a2c 0%, #c9a489 22%, #e8cdb6 45%, #d9867a 62%, #c4b5a8 80%, #3c5878 100%);
  }
  .hero-band {
    position: absolute; left: 0; top: 433px; width: 960px; height: 50px;
    background: var(--dark-band);
  }
  .brand-box {
    position: absolute; left: 81px; top: 409px; width: 254px; height: 74px;
    background: var(--red);
    display: flex; align-items: center; justify-content: center;
  }
  .brand-box .brand-name {
    font-family: 'Signika', sans-serif; font-weight: 300;
    font-size: 33px; color: var(--white); letter-spacing: 0.3px;
  }
  .service-note {
    position: absolute; left: 359px; top: 449px;
    font-family: 'Open Sans', sans-serif; font-size: 15px; color: var(--gold);
  }

  .section-title {
    position: absolute; left: 0; top: 540px; width: 960px; text-align: center;
    font-family: 'Signika', sans-serif; font-weight: 300; font-size: 38px;
    color: var(--ink); letter-spacing: 0.5px;
  }

  .profiles { position: absolute; left: 100px; top: 617px; display: flex; gap: 9px; }
  .profile { width: 87px; }
  .profile-photo { width: 87px; height: 90px; }
  .profile-name { margin-top: 6px; font-size: 10px; color: var(--label-grey); font-family: 'Roboto', sans-serif; }
  .profile-age { margin-top: 2px; font-size: 10px; color: var(--age-red); font-family: 'Roboto', sans-serif; }

  .block-title {
    font-family: 'Signika', sans-serif; font-weight: 300; font-size: 24px;
    color: var(--heading-brown);
  }
  .block-text { font-size: 10.5px; line-height: 13.6px; color: var(--body-grey); margin-top: 7px; }
  .about { position: absolute; left: 97px; top: 806px; width: 285px; }
  .rules { position: absolute; left: 97px; top: 947px; width: 285px; }

  .testimonials { position: absolute; left: 454px; top: 804px; width: 440px; }
  .avatar { position: absolute; left: 2px; top: 43px; width: 84px; height: 84px; border-radius: 50%;
    border: 2px solid #d8d8d8; overflow: hidden; }
  .avatar div { width: 100%; height: 100%; background: linear-gradient(180deg, #c8c8c8 0%, #d9b89c 50%, #4b5a70 100%); }
  .quote { position: absolute; left: 112px; top: 48px; width: 320px; font-size: 10.5px; line-height: 13.6px; color: var(--body-grey); }
  .author { position: absolute; left: 112px; top: 112px; font-family: 'Roboto', sans-serif; font-weight: 700; font-size: 13px; color: #6a6a6a; }
  .author-role { position: absolute; left: 112px; top: 130px; font-family: 'Roboto', sans-serif; font-weight: 700; font-size: 10.5px; color: #6a6a6a; }
  .dots { position: absolute; left: 112px; top: 157px; }

  .footer {
    position: absolute; left: 0; top: 1114px; width: 960px; height: 86px; background: var(--red);
  }
  .footer-brand {
    position: absolute; left: 110px; top: 30px;
    font-family: 'Signika', sans-serif; font-weight: 300; font-size: 21px; color: var(--white);
  }
  .footer-nav { position: absolute; left: 367px; top: 40px; display: flex; gap: 13px; }
  .footer-nav a { font-size: 10px; color: var(--white); text-decoration: none; }
  .footer-social { position: absolute; left: 794px; top: 39px; display: flex; gap: 10px; }
  .footer-social span { width: 12px; height: 12px; border-radius: 50%; background: var(--white); display: block; }
</style>
</head>
<body>

<div class="hero" role="img" aria-label="Photo of a man and a woman smiling over menus at a restaurant dinner"></div>
<div class="hero-band"></div>
<div class="brand-box"><span class="brand-name">Evening Company</span></div>
<p class="service-note">Dating service is only available in Geneva, Zurich and Basil Bern Switzerland.</p>

<h1 class="section-title">WHO‘S AVAILABLE FOR DATE</h1>

<div class="profiles">
  <div class="profile"><div class="profile-photo" role="img" aria-label="Portrait of Adriana" style="background:linear-gradient(135deg,#5a3a2e,#d9b4a0)"></div><p class="profile-name">ADRIANA</p><p class="profile-age">24 years old</p></div>
  <div class="profile"><div class="profile-photo" role="img" aria-label="Portrait of Natalie" style="background:linear-gradient(135deg,#3a2418,#c98a5a)"></div><p class="profile-name">NATALIE</p><p class="profile-age">20 years old</p></div>
  <div class="profile"><div class="profile-photo" role="img" aria-label="Portrait of Mark" style="background:linear-gradient(135deg,#c8b090,#6a4a3a)"></div><p class="profile-name">MARK</p><p class="profile-age">33 years old</p></div>
  <div class="profile"><div class="profile-photo" role="img" aria-label="Portrait of Elza" style="background:linear-gradient(135deg,#3c3a30,#d8b8a0)"></div><p class="profile-name">ELZA</p><p class="profile-age">24 years old</p></div>
  <div class="profile"><div class="profile-photo" role="img" aria-label="Portrait of Antonina" style="background:linear-gradient(135deg,#5a3a2e,#d9b4a0)"></div><p class="profile-name">ANTONINA</p><p class="profile-age">22 years old</p></div>
  <div class="profile"><div class="profile-photo" role="img" aria-label="Portrait of Max" style="background:linear-gradient(135deg,#3a2418,#c98a5a)"></div><p class="profile-name">MAX</p><p class="profile-age">30 years old</p></div>
  <div class="profile"><div class="profile-photo" role="img" aria-label="Portrait of Nelly" style="background:linear-gradient(135deg,#c8b090,#6a4a3a)"></div><p class="profile-name">NELLY</p><p class="profile-age">28 years old</p></div>
  <div class="profile"><div class="profile-photo" role="img" aria-label="Portrait of Adriana" style="background:linear-gradient(135deg,#3c3a30,#d8b8a0)"></div><p class="profile-name">ADRIANA</p><p class="profile-age">24 years old</p></div>
</div>

<section class="about">
  <h2 class="block-title">ABOUT US</h2>
  <p class="block-text">Lorem ipsum dolor sit consectetuer adipiscing Praesent vestibulum aenean nonummy hen- drerit. mauris. Hasellus porta. Fusce suscipit varius mi. Cum sociis natoque pnaibus et. Hasellus porta. Fusce sus- cipit varius mi. Cum sociis natoque pnaibus et magnis dis parturient montes nascetur ridiculus mus. Nulla dui.</p>
</section>

<section class="rules">
  <h2 class="block-title">RULES</h2>
  <p class="block-text">Lorem ipsum dolor sit consectetuer adipiscing Praesent vestibulum aenean nonummy hen- drerit. mauris. Hasellus porta. Fusce suscipit varius mi. Cum sociis natoque pnaibus et. Hasellus porta. Fusce sus- cipit varius mi. Cum sociis natoque pnaibus et magnis dis parturient montes nascetur ridiculus mus. Nulla dui.</p>
</section>

<section class="testimonials">
  <h2 class="block-title">OUR TESTIMONIALS</h2>
  <div class="avatar"><div role="img" aria-label="Portrait of a smiling man in a suit"></div></div>
  <p class="quote">Lorem ipsum dolor sit amet, consectetur adipisicing elit, sed do eiusmod tempor incididunt ut labore et dolore magna aliqua. Utenim ad minim veniam, quis nostrud exercitation ullamco laboris nisi ut aliquip ex ea commodo consequat.</p>
  <p class="author">Daniel Hartmann</p>
  <p class="author-role">Big Four firm</p>
  <svg class="dots" width="70" height="16" viewBox="0 0 70 16" aria-hidden="true">
    <circle cx="8" cy="8" r="7.5" fill="#d7001f"/>
    <circle cx="27" cy="8" r="5" fill="#7c8595"/>
    <circle cx="44" cy="8" r="5" fill="#7c8595"/>
    <circle cx="60" cy="8" r="5" fill="#7c8595"/>
  </svg>
</section>

<footer class="footer">
  <div class="footer-brand">Evening Company</div>
  <nav class="footer-nav">
    <a href="#">Home</a><a href="#">About us</a><a href="#">Rules</a><a href="#">Testimonials</a><a href="#">Join</a>
  </nav>
  <div class="footer-social" aria-label="Social links">
    <span></span><span></span><span></span><span></span>
  </div>
</footer>

</body>
</html>
```